Label design for an exciting new Vodka brand

We need a label design for a dynamic new Vodka brand called 'Pale lantern Vodka'. It is a crisp and versatile liquid with a clean and smooth finish. It should appeal to 21-39 year olds, with a slight female skew. Colours, fonts and styles should be modern and relatively neutral - take inspiration from the brand pictures attached.

Target Market(s)

21-39 year olds, both male and female, but with a slight female skew

```html
<!DOCTYPE html>
<html lang="en">
<head>
<meta charset="utf-8">
<title>Pale lantern Vodka – Label</title>
<link rel="stylesheet" href="https://fonts.googleapis.com/css2?family=Archivo:wdth,wght@125,800&family=Lexend:wght@200&display=swap">
<style>
  :root {
    --peach: #F3AC7A;
    --ember: #DA4E1B;
    --ink-light: #FFFFFF;
    --page: #FFFFFF;
  }
  html, body {
    margin: 0;
    padding: 0;
    width: 1200px;
    height: 1200px;
    overflow: hidden;
    background: var(--page);
  }
  .canvas {
    position: relative;
    width: 1200px;
    height: 1200px;
  }
  .label {
    position: absolute;
    left: 226px;
    top: 100px;
    width: 748px;
    height: 1000px;
    background: var(--peach);
    overflow: hidden;
  }
  .label__glow {
    position: absolute;
    inset: 0;
    width: 748px;
    height: 1000px;
  }
  .label__disc { fill: var(--ember); }
  .brand {
    position: absolute;
    left: 0;
    width: 748px;
    margin: 0;
    color: var(--ink-light);
    font-family: "Archivo", "Arial Black", sans-serif;
    font-weight: 800;
    font-stretch: 125%;
    font-variation-settings: "wdth" 125;
    line-height: 1;
    text-align: center;
    text-transform: uppercase;
    white-space: nowrap;
  }
  .brand__pale {
    top: 150px;
    font-size: 170px;
    letter-spacing: -0.02em;
  }
  .brand__lantern {
    top: 318px;
    font-size: 96px;
    letter-spacing: -0.01em;
  }
  .category {
    position: absolute;
    left: 0;
    top: 650px;
    width: 748px;
    margin: 0;
    padding-left: 0.42em;
    box-sizing: border-box;
    color: var(--ink-light);
    font-family: "Lexend", "Helvetica Neue", sans-serif;
    font-weight: 200;
    font-size: 90px;
    line-height: 1;
    letter-spacing: 0.42em;
    text-align: center;
    text-transform: uppercase;
    white-space: nowrap;
  }
</style>
</head>
<body>
  <main class="canvas">
    <section class="label">
      <svg class="label__glow" viewBox="0 0 748 1000" aria-hidden="true">
        <circle class="label__disc" cx="374" cy="700" r="270"/>
      </svg>
      <h1 class="brand brand__pale">Pale</h1>
      <p class="brand brand__lantern">Lantern</p>
      <p class="category">Vodka</p>
    </section>
  </main>
</body>
</html>
```